Sales brochure to promote delivery services

we need new revamped marketing brochure
We are a 3rd Party Logistics company specializing in home delivery and assembly for the home furnishings market. our company provides delivery services, we provide trained delivery teams, we also provide online order tracking, we provide routing and dispatching, expert handling of merchandise, white glove service. the brochure is going to be used for sales dept to leave/mail to potential customers. brochure is intended to give information about our services and attract business.

Target Market(s)

home furniture retailers, furniture and appliance retailers, retailers that require delivery services

Industry/Entity Type

Delivery Service

Requirements
Must have
• color scheme coordinates with company logo
• phone number 734.215-6043 and website address www.brakewell-3pl.com
Nice to have
• tri-fold design preferred
• include artwork and/or pictures related to our services examples would be dining room, living room, bedroom furniture, kitchen appliances, laundry, white box delivery truck, happy customers

```html
<!DOCTYPE html>
<html lang="en">
<head>
<meta charset="utf-8">
<title>Brakewell Logistics – Home Delivery &amp; Assembly Solutions</title>
<link href="https://fonts.googleapis.com/css2?family=Outfit:wght@400;500&display=swap" rel="stylesheet">
<style>
  :root{
    --purple:#524a7c;
    --ink:#4a4276;
    --yellow:#d6d23c;
    --white:#ffffff;
  }
  *{margin:0;padding:0;box-sizing:border-box}
  html,body{width:1200px;height:934px;overflow:hidden;background:#fff}
  .brochure{position:relative;width:1200px;height:934px;overflow:hidden;font-family:"Outfit",sans-serif;font-weight:500;color:var(--ink)}
  .backdrop{position:absolute;inset:0}
  .abs{position:absolute}
  .intro{left:43px;top:136px;font-size:21px;line-height:27px}
  .benefits{left:43px;top:268px;list-style:none;font-size:19.5px;line-height:26px}
  .benefits li,.values li{position:relative;padding-left:20px}
  .benefits li{margin-bottom:19px}
  .benefits li::before,.values li::before{content:"";position:absolute;left:2px;top:10px;width:7px;height:7px;border-radius:50%;background:currentColor}
  .wordmark{color:var(--ink);white-space:nowrap}
  .wordmark-small{left:510px;top:110px;font-size:15px}
  .wordmark-large{left:812px;top:146px;font-size:30px}
  .tagline{left:414px;width:360px;text-align:center;font-size:22.5px;line-height:29px}
  .tagline-one{top:228px}
  .tagline-two{top:332px}
  .title{left:788px;width:400px;text-align:center;font-size:29px;line-height:37px;top:384px;font-weight:500}
  .panel-text{color:var(--white)}
  .values-head{left:43px;top:574px;font-size:19.5px}
  .values{left:43px;top:624px;list-style:none;font-size:19.5px;line-height:26px}
  .values li{margin-bottom:17px}
  .slogan{left:414px;width:360px;top:594px;text-align:center;font-size:37px;line-height:45px}
  .company{left:435px;top:744px;font-size:19px}
  .address{left:435px;top:787px;font-size:17px;line-height:21.5px}
  .contact{left:435px;top:851px;font-size:17px;line-height:22px}
  .help{left:20px;width:362px;top:836px;text-align:center;font-size:24px;line-height:31px}
  .back-contact{left:800px;width:392px;text-align:center;font-size:20px;top:826px;line-height:43px;letter-spacing:.5px}
</style>
</head>
<body>
<div class="brochure">
  <svg class="backdrop" width="1200" height="934" viewBox="0 0 1200 934">
    <defs>
      <linearGradient id="city" x1="0" y1="0" x2="1" y2="1">
        <stop offset="0" stop-color="#f3f4f8"/>
        <stop offset=".5" stop-color="#d2d6e6"/>
        <stop offset="1" stop-color="#e8eaf2"/>
      </linearGradient>
    </defs>
    <rect width="1200" height="700" fill="url(#city)" role="img" aria-label="Photo of a misty city skyline at night with light trails of moving traffic"/>
    <polygon points="0,462 100,524 544,452 1012,676 1200,548 1200,934 0,934" fill="var(--yellow)"/>
    <polygon points="0,480 100,534 544,468 1012,690 1200,566 1200,934 0,934" fill="var(--purple)"/>
  </svg>

  <p class="abs intro">Our team of improvement<br>professionals will help you<br>with the areas that mean the<br>most to your business:</p>
  <ul class="abs benefits">
    <li>Higher on-time delivery</li>
    <li>Lower Exchanges &amp; Damages</li>
    <li>Greater Customer Satisfaction</li>
  </ul>

  <div class="abs wordmark wordmark-small">Brakewell Logistics</div>
  <p class="abs tagline tagline-one">Brakewell is what happens<br>when you get moving...</p>
  <p class="abs tagline tagline-two">Building Brakewell is<br>following one success<br>immediately with another.</p>

  <div class="abs wordmark wordmark-large">Brakewell Logistics</div>
  <h1 class="abs title">HOME DELIVERY &amp;<br>ASSEMBLY SOLUTIONS</h1>

  <p class="abs panel-text values-head">At BRAKEWELL We:</p>
  <ul class="abs panel-text values">
    <li>Practice a simple no-nonsense<br>approach to problem solving</li>
    <li>Are efficient, resourceful and<br>thorough</li>
  </ul>
  <p class="abs panel-text help">We’re Here to Help You<br>Improve Your Bottom Line</p>

  <p class="abs panel-text slogan">When You Win,<br>We Win!</p>
  <p class="abs panel-text company">BRAKEWELL3PL, INC.</p>
  <p class="abs panel-text address">14 Harborline Way Suite 210<br>Fairbrook CA 90481</p>
  <p class="abs panel-text contact">Tel: 734.215-6043<br>Website: www.brakewell-3pl.com</p>

  <p class="abs panel-text back-contact">TEL: 734-215-6043<br>WWW.BRAKEWELL-3PL.COM</p>
</div>
</body>
</html>
```